Graduation Yearbook Page for a Young Lady

A one page for my daughter's yearbook. She is in 8th grade, which in her school is the year they graduate and go to different highschools. I am looking for a clean and elegant and yet imaginative layout that incorporates "Tessa, Congratulations, We are so very proud of you. Mom, Dad, Grandma, Joan and Harold.
Please feel free as many or as few as 4 of the attached photos. The main photo Tessa Smiling should be in the center.

```html
<!DOCTYPE html>
<html lang="en">
<head>
<meta charset="utf-8">
<title>Tessa – Graduation Yearbook Page</title>
<link rel="stylesheet" href="https://fonts.googleapis.com/css2?family=Federo&display=swap">
<style>
  :root {
    --rust: #bf4a1d;
    --rust-light: #e0661f;
    --teal: #2f706c;
    --teal-light: #4a8c85;
    --teal-deep: #0f4745;
    --ink: #05080b;
    --sun: #f7b521;
    --stone: #6f7478;
    --aqua-text: #5bb7c0;
  }
  html, body {
    margin: 0;
    padding: 0;
    width: 848px;
    height: 1200px;
    overflow: hidden;
    background: var(--rust);
  }
  .page {
    display: block;
    width: 848px;
    height: 1200px;
  }
  .headline, .greeting, .message, .signature {
    font-family: "Federo", "Poiret One", sans-serif;
  }
  .headline { fill: var(--sun); font-size: 220px; }
  .greeting { fill: var(--sun); font-size: 64px; }
  .message { fill: var(--aqua-text); font-size: 50px; }
  .signature { fill: var(--aqua-text); font-size: 30px; }
  .shadow { fill: var(--ink); }
</style>
</head>
<body>
<svg class="page" viewBox="0 0 800 1132" width="848" height="1200" xmlns="http://www.w3.org/2000/svg">
  <defs>
    <linearGradient id="teal-wash" x1="0" y1="0" x2="1" y2="1">
      <stop offset="0" stop-color="var(--teal)"/>
      <stop offset="1" stop-color="var(--teal-light)"/>
    </linearGradient>
    <linearGradient id="portrait-tone" x1="0" y1="0" x2="1" y2="1">
      <stop offset="0" stop-color="#1a120e"/>
      <stop offset="0.45" stop-color="#b46a3c"/>
      <stop offset="1" stop-color="#8c8a6e"/>
    </linearGradient>
    <radialGradient id="child-tone" cx="0.5" cy="0.45" r="0.6">
      <stop offset="0" stop-color="#d9a886"/>
      <stop offset="1" stop-color="#3a2a22"/>
    </radialGradient>
    <linearGradient id="beach-tone" x1="0" y1="0" x2="0" y2="1">
      <stop offset="0" stop-color="#dcd8d0"/>
      <stop offset="0.6" stop-color="#c98a7a"/>
      <stop offset="1" stop-color="#d8413f"/>
    </linearGradient>
    <linearGradient id="summer-tone" x1="0" y1="0" x2="1" y2="0">
      <stop offset="0" stop-color="#e8ddd0"/>
      <stop offset="0.6" stop-color="#c79a6e"/>
      <stop offset="1" stop-color="#3f6a3a"/>
    </linearGradient>
  </defs>

  <!-- background -->
  <rect class="field" width="800" height="1132" fill="var(--rust)"/>
  <path class="field-glow" d="M0 760 C150 650 400 680 560 720 C680 750 760 780 800 800 L800 980 L0 980 Z" fill="var(--rust-light)" opacity="0.8"/>

  <!-- left teal wave -->
  <path class="wave-left" d="M0 60 C90 90 180 200 175 330 C170 470 90 560 0 610 Z" fill="url(#teal-wash)" stroke="var(--ink)" stroke-width="14"/>

  <!-- right teal wave -->
  <path class="wave-right" d="M335 0 C320 140 390 250 470 330 C540 400 560 520 600 600 C640 680 720 715 800 720 L800 0 Z" fill="url(#teal-wash)" stroke="var(--ink)" stroke-width="16"/>

  <!-- bottom teal wave -->
  <path class="wave-bottom" d="M0 880 C120 870 230 880 300 905 C370 930 420 960 500 965 C580 970 650 1010 710 1060 C740 1090 750 1115 760 1132 L0 1132 Z" fill="var(--teal-deep)" stroke="var(--ink)" stroke-width="14"/>

  <!-- accent dots -->
  <circle class="dot-sun" cx="762" cy="12" r="58" fill="var(--sun)" stroke="var(--ink)" stroke-width="14"/>
  <circle class="dot-sun" cx="22" cy="935" r="62" fill="var(--sun)" stroke="var(--ink)" stroke-width="14"/>
  <circle class="dot-stone" cx="45" cy="18" r="52" fill="var(--stone)" stroke="var(--ink)" stroke-width="14"/>
  <circle class="dot-stone" cx="772" cy="760" r="42" fill="var(--stone)" stroke="var(--ink)" stroke-width="12"/>
  <circle class="dot-stone" cx="765" cy="1095" r="46" fill="var(--stone)" stroke="var(--ink)" stroke-width="12"/>

  <!-- main portrait -->
  <g class="portrait-main" transform="rotate(-12 615 335)">
    <rect x="445" y="90" width="360" height="490" fill="var(--ink)"/>
    <rect x="455" y="100" width="340" height="470" fill="url(#portrait-tone)" role="img" aria-label="Portrait photo of Tessa smiling, wearing a light scarf"/>
  </g>

  <!-- childhood photos -->
  <circle class="frame-ring" cx="225" cy="665" r="152" fill="var(--ink)"/>
  <circle class="photo-childhood" cx="225" cy="665" r="138" fill="url(#child-tone)" role="img" aria-label="Photo of Tessa as a young child"/>

  <circle class="frame-ring" cx="478" cy="800" r="105" fill="var(--ink)"/>
  <circle class="photo-beach" cx="478" cy="800" r="93" fill="url(#beach-tone)" role="img" aria-label="Photo of Tessa on a beach holding an ice cream sundae"/>

  <circle class="frame-ring" cx="688" cy="892" r="97" fill="var(--ink)"/>
  <circle class="photo-summer" cx="688" cy="892" r="85" fill="url(#summer-tone)" role="img" aria-label="Photo of Tessa outdoors wearing sunglasses"/>

  <!-- headline -->
  <text class="headline shadow" x="86" y="339" textLength="330" lengthAdjust="spacingAndGlyphs">TESSA</text>
  <text class="headline" x="80" y="333" textLength="330" lengthAdjust="spacingAndGlyphs">TESSA</text>
  <text class="greeting shadow" x="21" y="421" textLength="460" lengthAdjust="spacingAndGlyphs">CONGRATULATIONS!</text>
  <text class="greeting" x="18" y="418" textLength="460" lengthAdjust="spacingAndGlyphs">CONGRATULATIONS!</text>

  <!-- message -->
  <text class="message" x="78" y="995" textLength="297" lengthAdjust="spacingAndGlyphs">WE ARE SO VERY</text>
  <text class="message" x="90" y="1040" textLength="282" lengthAdjust="spacingAndGlyphs">PROUD OF YOU.</text>
  <text class="signature" x="78" y="1097" textLength="529" lengthAdjust="spacingAndGlyphs">MOM, DAD, GRANDMA, JOAN AND HAROLD.</text>
</svg>
</body>
</html>
```